Flyers

Modify Existing Flyer and create another for exterior company
Updates

Previous Brief has been updated- we want to update this existing one also

Target Market(s)

Exterior Remodeling Customers

Industry/Entity Type

Remodeling/Construction

```html
<!DOCTYPE html>
<html lang="en">
<head>
<meta charset="utf-8">
<title>Northfield Roofing and Exteriors – Remodeling Flyer</title>
<link rel="stylesheet" href="https://fonts.googleapis.com/css2?family=Montserrat:wght@500;600;700;800&family=Open+Sans:wght@400;600&display=swap">
<style>
  :root {
    --orange: #e8892b;
    --charcoal: #2b2b2b;
    --charcoal-deep: #1f1f1f;
    --band: rgba(40,40,40,0.88);
    --white: #ffffff;
    --muted: #d9d9d9;
    --kitchen-light: #d9cfc2;
    --kitchen-dark: #6b5a48;
  }
  * { margin: 0; padding: 0; box-sizing: border-box; }
  html, body { width: 847px; height: 1200px; overflow: hidden; background: #fff; }
  .flyer { position: relative; width: 847px; height: 1200px; overflow: hidden; font-family: "Open Sans", sans-serif; color: var(--white); background: var(--charcoal); }

  .header { position: absolute; left: 0; top: 0; width: 847px; height: 112px; background: var(--white); }
  .brand { position: absolute; left: 26px; top: 24px; display: flex; align-items: center; gap: 12px; }
  .brand-mark { width: 40px; height: 40px; background: var(--orange); border-radius: 50%; }
  .brand-name { font-family: "Montserrat", sans-serif; font-weight: 700; font-size: 17px; color: var(--charcoal); line-height: 1.2; width: 190px; text-transform: uppercase; }

  .estimate { position: absolute; left: 510px; top: 0; width: 337px; height: 112px; background: var(--charcoal-deep); }
  .estimate-lead { position: absolute; left: 62px; top: 16px; font-family: "Montserrat", sans-serif; font-weight: 600; font-size: 19px; line-height: 1.15; text-transform: uppercase; }
  .estimate-lead span { display: block; color: var(--white); font-weight: 700; }
  .estimate-lead em { font-style: normal; text-transform: none; font-size: 18px; }
  .estimate-phone { position: absolute; left: 62px; top: 66px; display: flex; align-items: center; gap: 14px; font-family: "Montserrat", sans-serif; font-weight: 600; font-size: 21px; }
  .phone-badge { width: 34px; height: 34px; border-radius: 50%; background: var(--white); display: flex; align-items: center; justify-content: center; }

  .hero { position: absolute; left: 0; top: 112px; width: 847px; height: 536px; }
  .hero-kitchen { position: absolute; left: 0; top: 0; width: 610px; height: 536px; background: linear-gradient(180deg, #cfc4b6 0%, #b9aa98 45%, #7d6a56 75%, #4a3d31 100%); }
  .hero-living { position: absolute; left: 610px; top: 0; width: 237px; height: 536px; background: linear-gradient(160deg, #4a4440 0%, #6d5a4a 50%, #8a6f58 75%, #3b2f27 100%); }

  .hero-title { position: absolute; left: 20px; top: 378px; font-family: "Montserrat", sans-serif; font-weight: 600; font-size: 29px; line-height: 1.15; color: var(--white); text-shadow: 0 1px 4px rgba(0,0,0,0.45); }
  .hero-title strong { font-weight: 800; font-size: 33px; }
  .hero-title .accent { color: var(--orange); }
  .hero-band { position: absolute; left: 0; top: 470px; width: 847px; height: 66px; background: var(--band); display: flex; align-items: center; padding-left: 20px; }
  .hero-band h2 { font-family: "Montserrat", sans-serif; font-weight: 500; font-size: 26px; line-height: 1.05; text-transform: uppercase; letter-spacing: 0.2px; width: 760px; }

  .services { position: absolute; left: 0; top: 648px; width: 847px; height: 552px; background: linear-gradient(180deg, #2f2f2f 0%, #3a3632 55%, #2a2724 100%); }
  .service { position: absolute; }
  .service-photo { position: absolute; background: linear-gradient(160deg, #8d8378, #4d4640); }
  .service-heading { display: flex; align-items: center; gap: 8px; font-family: "Montserrat", sans-serif; font-weight: 700; font-size: 15px; text-transform: uppercase; margin-bottom: 6px; }
  .service-heading svg { flex: none; }
  .service p { font-size: 9.5px; line-height: 1.35; color: var(--muted); margin-bottom: 8px; }
  .service ul { list-style: none; }
  .service li { font-size: 10px; line-height: 1.55; color: var(--white); padding-left: 12px; position: relative; }
  .service li::before { content: ""; position: absolute; left: 0; top: 6px; width: 4px; height: 4px; border-radius: 50%; background: var(--white); }

  .kitchen-photo { left: 23px; top: 25px; width: 152px; height: 177px; background: linear-gradient(160deg, #5a5a5c, #2c2c2e); }
  .kitchen-copy { left: 200px; top: 2px; width: 230px; }
  .additions-photo { left: 453px; top: 60px; width: 155px; height: 169px; background: linear-gradient(160deg, #6a5f55, #3a332d); }
  .additions-copy { left: 632px; top: 82px; width: 200px; }
  .bath-photo { left: 23px; top: 252px; width: 152px; height: 162px; background: linear-gradient(160deg, #9a948c, #55504a); }
  .bath-copy { left: 200px; top: 256px; width: 230px; }
  .decks-photo { left: 453px; top: 294px; width: 155px; height: 176px; background: linear-gradient(160deg, #7f8a6a, #4b4538); }
  .decks-copy { left: 632px; top: 314px; width: 200px; }

  .website { position: absolute; left: 0; top: 1136px; width: 847px; text-align: center; font-size: 14px; color: var(--white); }
</style>
</head>
<body>
<div class="flyer">
  <header class="header">
    <div class="brand">
      <div class="brand-mark"></div>
      <div class="brand-name">Northfield Roofing and Exteriors</div>
    </div>
    <div class="estimate">
      <div class="estimate-lead">
        <span>Call today for your</span>
        <em style="color:var(--orange)">Free Estimate</em>
      </div>
      <div class="estimate-phone">
        <div class="phone-badge">
          <svg width="18" height="18" viewBox="0 0 24 24"><path fill="#1f1f1f" d="M6.6 10.8a15.1 15.1 0 0 0 6.6 6.6l2.2-2.2a1 1 0 0 1 1-.25 11.4 11.4 0 0 0 3.6.57 1 1 0 0 1 1 1V20a1 1 0 0 1-1 1A17 17 0 0 1 3 4a1 1 0 0 1 1-1h3.5a1 1 0 0 1 1 1c0 1.25.2 2.45.57 3.57a1 1 0 0 1-.25 1z"/></svg>
        </div>
        515-555-0148
      </div>
    </div>
  </header>

  <section class="hero">
    <div class="hero-kitchen" role="img" aria-label="Bright remodeled kitchen with white cabinets, island and pendant lights"></div>
    <div class="hero-living" role="img" aria-label="Warm living room corner with armchair and lamp"></div>
    <h1 class="hero-title">Ready for a Beautiful and Functional<br><strong><span class="accent">Kitchen</span> or <span class="accent">Bathroom</span>?</strong></h1>
    <div class="hero-band"><h2>Work with a top-rated local remodeling company in Ankeny, AI</h2></div>
  </section>

  <section class="services">
    <div class="service service-photo kitchen-photo" role="img" aria-label="Modern kitchen remodel"></div>
    <div class="service kitchen-copy">
      <div class="service-heading">
        <svg width="20" height="20" viewBox="0 0 24 24"><path fill="none" stroke="#fff" stroke-width="2" d="M3 11l9-7 9 7v9H3z"/></svg>
        Kitchen Remodeling
      </div>
      <p>Whatever your vision is for your new kitchen, our crew can help you bring it to life. You can trust us for:</p>
      <ul>
        <li>Open-concept design services</li>
        <li>Kitchen cabinet installation services</li>
        <li>Kitchen countertop installation services</li>
        <li>Tile installation services</li>
        <li>Lightening installation services</li>
        <li>Plumbing upgrade services</li>
        <li>Electrical upgrade services</li>
        <li>Drywall services</li>
        <li>Painting services</li>
      </ul>
    </div>

    <div class="service service-photo additions-photo" role="img" aria-label="Finished home addition interior"></div>
    <div class="service additions-copy">
      <div class="service-heading">
        <svg width="20" height="20" viewBox="0 0 24 24"><path fill="none" stroke="#fff" stroke-width="2" d="M3 11l9-7 9 7v9H3z"/></svg>
        Home Additions
      </div>
      <p>No matter what kind of space you need, our team will bring your vision to life. You can trust us if you need a:</p>
      <ul>
        <li>Bathroom addition</li>
        <li>Bedroom addition</li>
        <li>Garage addition</li>
        <li>Basement addition</li>
        <li>Guest room addition</li>
        <li>Living room addition</li>
        <li>Sunroom addition</li>
      </ul>
    </div>

    <div class="service service-photo bath-photo" role="img" aria-label="Remodeled bathroom with vanity"></div>
    <div class="service bath-copy">
      <div class="service-heading">
        <svg width="20" height="20" viewBox="0 0 24 24"><path fill="none" stroke="#fff" stroke-width="2" d="M3 11l9-7 9 7v9H3z"/></svg>
        Bathroom Remodeling
      </div>
      <p>When you hire us for your bathroom remodeling project, the possibilities are endless. Our experienced and talented team can:</p>
      <ul>
        <li>Install a custom tile shower</li>
        <li>Build a new vanity</li>
        <li>Install flooring and tile</li>
        <li>Replace your plumbing and light fixtures</li>
      </ul>
    </div>

    <div class="service service-photo decks-photo" role="img" aria-label="Backyard deck and patio with seating"></div>
    <div class="service decks-copy">
      <div class="service-heading">
        <svg width="20" height="20" viewBox="0 0 24 24"><path fill="none" stroke="#fff" stroke-width="2" d="M3 11l9-7 9 7v9H3z"/></svg>
        Decks/Patios
      </div>
      <p>An outdoor space is a great addition to any residential property. When you decide to build a patio or deck, you'll be able to experience a variety of benefits. Your outdoor area will increase your:</p>
      <ul>
        <li>Property value</li>
        <li>Curb appeal</li>
        <li>Functional living space</li>
      </ul>
    </div>

    <div class="website" style="top:488px">www.northfieldext.com</div>
  </section>
</div>
</body>
</html>
```